Software Company Business Card

We are looking for a new design of our business card. The design will also be used in the rest of our branding and marketing materials as we want to keep it all uniform. We sell POS software to fine/luxury jewelers and also offer other business services as well to help the jeweler manage their business and need something more updated, technical and fresh, preferably more on the masculine side. We do not want any designs with gems in them but if possible would like to incorporate the circle and arrow in the logo into the design, but not a requirement if you can't make it work. I would like to see a variety of the mix. The colors need to remain our blue and orange and the logo can not change. The squiggly lines have been used as our corporate identity for over 20 years and its time to update. Our company name is PELK (Bright Ledger Counter Solutions).

Target Market(s)

High End Jewelers

Industry/Entity Type

Software

Contact Information for Business Card

Requirements
Must have
• Our logo and the colors must remain the same. Blue is #d95d39 and Orange is #0f5682.
Nice to have
• The circle and arrow incorporated but not a requirement.
Should not have
• Anything jewelry or gem related.

```html
<!DOCTYPE html>
<html lang="en">
<head>
<meta charset="utf-8">
<title>PELK Business Card</title>
<link href="https://fonts.googleapis.com/css2?family=Poppins:wght@400;500;600;700&display=swap" rel="stylesheet">
<style>
  :root {
    --brand-blue: #0f4f7e;
    --brand-blue-light: #5b8db4;
    --brand-blue-mid: #2d6a98;
    --brand-orange: #d95d39;
    --accent-peach: #f5dfd7;
    --paper: #ffffff;
    --backdrop: #ebebeb;
    --pattern-tone: #2a6492;
  }
  * { margin: 0; padding: 0; box-sizing: border-box; }
  html, body { width: 1200px; height: 1200px; overflow: hidden; }
  body {
    background: var(--backdrop);
    font-family: "Poppins", sans-serif;
    position: relative;
  }
  .card {
    position: absolute;
    left: 190px;
    width: 820px;
    height: 469px;
    overflow: hidden;
    box-shadow: 0 6px 20px rgba(0,0,0,0.12);
  }
  .card--front { top: 95px; background: var(--paper); }
  .card--back  { top: 636px; background: var(--brand-blue); }

  .front__accent-circle {
    position: absolute;
    left: -40px; top: -70px;
    width: 300px; height: 300px;
    border-radius: 50%;
    background: var(--accent-peach);
  }
  .front__stripe-light {
    position: absolute; left: 0; right: 0;
    top: 150px; height: 30px;
    background: var(--brand-blue-light);
    transform: skewY(-3.2deg); transform-origin: right top;
    opacity: .85;
  }
  .front__stripe-mid {
    position: absolute; left: 0; right: 0;
    top: 168px; height: 26px;
    background: var(--brand-blue-mid);
    transform: skewY(-3.2deg); transform-origin: right top;
  }
  .front__band {
    position: absolute; left: 0; right: 0;
    top: 186px; height: 234px;
    background: var(--brand-blue);
    transform: skewY(-3.2deg); transform-origin: right top;
  }
  .brand {
    position: absolute;
    display: flex; align-items: center; gap: 10px;
  }
  .brand__name {
    font-weight: 700;
    letter-spacing: 1px;
    line-height: 1;
  }
  .brand__dot { border-radius: 50%; background: var(--brand-orange); }
  .front .brand { right: 60px; top: 42px; }
  .front .brand__name { font-size: 54px; color: var(--brand-blue); }
  .front .brand__dot { width: 48px; height: 48px; }

  .holder { position: absolute; left: 72px; top: 240px; color: #fff; }
  .holder__name { font-size: 25px; font-weight: 700; letter-spacing: .5px; line-height: 1.1; }
  .holder__title { font-size: 16px; font-weight: 500; }

  .contacts {
    position: absolute; left: 72px; top: 322px;
    list-style: none; color: #fff; font-size: 14.5px; line-height: 1.45;
  }
  .contacts li { display: flex; align-items: center; gap: 8px; }
  .contacts svg { width: 14px; height: 14px; flex: none; }

  .address {
    position: absolute; left: 330px; top: 304px;
    display: flex; gap: 10px; color: #fff; font-size: 14.5px; line-height: 1.35;
  }
  .address svg { width: 20px; height: 20px; flex: none; margin-top: 2px; }

  .back__pattern {
    position: absolute; inset: 24px;
    background: radial-gradient(circle, var(--pattern-tone) 0%, var(--brand-blue) 100%);
    opacity: .8;
  }
  .back .brand { left: 50%; top: 50%; transform: translate(-50%, -50%); }
  .back .brand__name { font-size: 84px; color: #fff; }
  .back .brand__dot { width: 62px; height: 62px; }
</style>
</head>
<body>
  <section class="card card--front front">
    <div class="front__accent-circle"></div>
    <div class="front__stripe-light"></div>
    <div class="front__stripe-mid"></div>
    <div class="front__band"></div>

    <div class="brand">
      <span class="brand__name">PELK</span>
      <span class="brand__dot"></span>
    </div>

    <div class="holder">
      <p class="holder__name">DORIAN WHITCOMBE</p>
      <p class="holder__title">Director of Global Operations</p>
    </div>

    <ul class="contacts">
      <li><svg viewBox="0 0 14 14"><circle cx="7" cy="7" r="7" fill="#d95d39"/><path d="M4.5 3.8l1.3-.3.7 1.7-.8.6a5 5 0 0 0 2.5 2.5l.6-.8 1.7.7-.3 1.3c-3.3.3-6-2.4-5.7-5.7z" fill="#fff"/></svg>+1 800 555-0142</li>
      <li><svg viewBox="0 0 14 14"><circle cx="7" cy="7" r="7" fill="#d95d39"/><rect x="4" y="5" width="6" height="5" rx="1" fill="#fff"/><rect x="5" y="3.5" width="4" height="2" fill="#fff"/></svg>+1 702 555-0187</li>
      <li><svg viewBox="0 0 14 14"><circle cx="7" cy="7" r="7" fill="#d95d39"/><rect x="3.5" y="4.5" width="7" height="5" fill="#fff"/><path d="M3.5 4.5L7 7.3l3.5-2.8" stroke="#d95d39" stroke-width=".8" fill="none"/></svg>dorian@pelkusa.com</li>
      <li><svg viewBox="0 0 14 14"><circle cx="7" cy="7" r="7" fill="#d95d39"/><circle cx="7" cy="7" r="3.6" fill="none" stroke="#fff" stroke-width=".9"/><path d="M3.4 7h7.2M7 3.4v7.2" stroke="#fff" stroke-width=".8"/></svg>www.pelkusa.com</li>
    </ul>

    <div class="address">
      <svg viewBox="0 0 20 20"><circle cx="10" cy="10" r="10" fill="#fff"/><path d="M10 4.5a3.5 3.5 0 0 0-3.5 3.5c0 2.6 3.5 7 3.5 7s3.5-4.4 3.5-7A3.5 3.5 0 0 0 10 4.5z" fill="#0f4f7e"/><circle cx="10" cy="8" r="1.3" fill="#fff"/></svg>
      <p>1480 Meridian Court<br>Suite 210<br>Lakemont, NV 89011<br>USA</p>
    </div>
  </section>

  <section class="card card--back back">
    <div class="back__pattern" role="img" aria-label="Repeating tone-on-tone pattern of brand circles across the card back"></div>
    <div class="brand">
      <span class="brand__name">PELK</span>
      <span class="brand__dot"></span>
    </div>
  </section>
</body>
</html>
```